Kralto website design on shopify

Job Description:
As a web designer for Kralto, you will be the driving force behind designing and developing our new e-commerce website. Your responsibility will be to create an attractive, functional, and intuitive online shopping experience where customers can effortlessly discover and purchase high-quality supplements such as pre-workout, creatine, and protein shakes. Your design will play a crucial role in enhancing our brand and engaging our target audience.

Coding

Coded - Design and coding required

```html
<!DOCTYPE html>
<html lang="en">
<head>
<meta charset="utf-8">
<title>Kralto — Fueling Health, Not Expenses</title>
<link href="https://fonts.googleapis.com/css2?family=Merriweather:wght@400;700;900&family=Lato:wght@400;700&family=Poppins:wght@400;500;600&display=swap" rel="stylesheet">
<style>
:root{
  --ink:#1c1c1c;
  --dark:#262626;
  --purple:#7b2a8a;
  --lilac:#e2cfe6;
  --red:#ea4a4c;
  --foot:#f4f4f4;
  --muted:#444;
  --white:#fff;
}
*{margin:0;padding:0;box-sizing:border-box}
html,body{width:1200px;height:3631px;overflow:hidden;background:var(--white);color:var(--ink);font-family:"Lato",sans-serif}
.page{position:relative;width:1200px;height:3631px}
.abs{position:absolute}
.serif{font-family:"Merriweather",serif}

.topbar{left:0;top:0;width:1200px;height:49px;background:var(--dark);color:var(--white)}
.socials{position:absolute;display:flex;gap:12px;align-items:center}
.socials span{width:14px;height:14px;border-radius:50%;background:currentColor;display:block}
.topbar .socials{left:99px;top:17px}
.wholesale{right:120px;top:14px;font-family:"Merriweather",serif;font-size:15px;display:flex;align-items:center;gap:10px}
.cart-count{display:inline-block;width:17px;height:17px;border-radius:50%;background:#fff;color:var(--dark);font-size:10px;text-align:center;line-height:17px;margin-left:-8px;margin-top:-14px}

.nav{left:0;top:49px;width:1200px;height:86px;background:var(--white)}
.brand{left:99px;top:22px;display:flex;align-items:center;gap:10px;font-family:"Merriweather",serif;font-weight:700;font-size:28px;color:var(--purple)}
.brand i{width:34px;height:34px;border-radius:50%;border:2px solid var(--purple);display:block}
.nav ul{position:absolute;left:350px;top:33px;display:flex;gap:34px;list-style:none;font-family:"Merriweather",serif;font-size:15px;color:#333}

.promo{left:0;top:135px;width:1200px;height:43px;background:var(--purple);color:#fff;text-align:center;font-family:"Merriweather",serif;font-size:15px;line-height:43px}

.hero{left:0;top:178px;width:1200px;height:600px;background:linear-gradient(180deg,#5d6b72 0%,#8a969b 55%,#6e7679 100%)}
.tub{position:absolute;border-radius:40px 40px 20px 20px}
.tub.light{left:228px;top:47px;width:282px;height:505px;background:linear-gradient(90deg,#d9d9d9,#f3f3f3 50%,#cfcfcf)}
.tub.dark{left:688px;top:47px;width:286px;height:505px;background:linear-gradient(90deg,#111,#3a3a3a 50%,#0e0e0e)}
.hero h1{position:absolute;left:0;width:1200px;top:218px;text-align:center;font-family:"Merriweather",serif;font-weight:900;font-size:48px;color:#111}
.hero p{position:absolute;left:0;width:1200px;top:290px;text-align:center;font-size:15px;color:#fff}
.btn{display:block;text-align:center;font-family:"Merriweather",serif;font-weight:700;color:#fff;background:var(--purple)}
.hero .btn{position:absolute;left:513px;top:325px;width:175px;height:53px;line-height:53px;font-size:16px}

.cat{top:839px;width:309px;height:433px;background:var(--lilac)}
.cat .bottle{position:absolute;left:80px;top:47px;width:150px;height:326px;border-radius:30px;background:linear-gradient(90deg,#cdd3d6,#f4f6f7 50%,#c8ced1)}
.cat h3{position:absolute;left:0;width:100%;top:214px;text-align:center;font-family:"Merriweather",serif;font-weight:700;font-size:19px;color:#111}
.cat .btn{position:absolute;left:86px;top:258px;width:137px;height:51px;line-height:51px;font-size:15px}

.sec-title{left:0;width:1200px;text-align:center;font-family:"Merriweather",serif;font-weight:900;font-size:33px;color:#111}
.rule{left:527px;width:146px;height:4px;background:var(--purple)}
.viewall{left:0;width:1200px;top:1406px;text-align:center;font-family:"Merriweather",serif;font-size:16px;text-decoration:underline;color:#222}

.prod{top:1455px;width:240px}
.prod .ph{height:322px;background:var(--lilac);position:relative}
.prod .ph b{position:absolute;left:40px;top:60px;right:40px;bottom:70px;border-radius:14px;background:linear-gradient(135deg,#3a2a4a,#1c1c22)}
.prod .name{margin-top:18px;text-align:center;font-family:"Merriweather",serif;font-size:16px;color:#222}
.prod .price{margin-top:10px;text-align:center;font-family:"Merriweather",serif;font-size:16px;color:#222}
.zoom{position:absolute;right:14px;top:26px;width:40px;height:40px;border-radius:50%;background:#fff}
.arrow{width:40px;height:40px;border-radius:50%;background:#fff;box-shadow:0 1px 4px rgba(0,0,0,.2);top:1596px}

.feature{left:0;top:1918px;width:1200px;height:592px;background:var(--lilac)}
.photo1{left:99px;top:82px;width:306px;height:387px;background:linear-gradient(135deg,#cfc6bd,#e8dcd2 60%,#b8ada3)}
.photo2{left:382px;top:124px;width:308px;height:388px;background:linear-gradient(135deg,#e4e0d8,#cfc2b2 55%,#7e8a86)}
.feature h2{position:absolute;left:729px;top:157px;font-family:"Merriweather",serif;font-weight:900;font-size:33px;line-height:42px;color:#111}
.feature p{position:absolute;left:731px;top:242px;width:370px;font-size:15px;line-height:31px;color:#333}
.btn-red{position:absolute;left:730px;top:410px;width:139px;height:51px;line-height:51px;background:var(--red);font-size:15px;box-shadow:0 2px 4px rgba(0,0,0,.2)}

.post{top:2672px;width:317px;text-align:center}
.post .ph{height:260px}
.post h4{margin-top:18px;font-family:"Merriweather",serif;font-weight:900;font-size:19px;color:#111}
.post p{margin-top:6px;font-size:15px;line-height:31px;color:#333}

.thanks{left:0;top:3099px;width:1200px;height:51px;background:var(--purple);color:#fff;text-align:center;line-height:51px;font-size:15px;font-weight:700;letter-spacing:.2px}

.footer{left:0;top:3150px;width:1200px;height:481px;background:var(--foot);color:#222}
.footer .socials{left:546px;top:42px;color:#111;gap:20px}
.footer .socials span{width:12px;height:12px}
.col{top:96px;font-size:15px;line-height:31px;color:#333}
.col h5{font-family:"Poppins",sans-serif;font-weight:600;font-size:20px;color:#111;margin-bottom:4px;line-height:30px}
.email{left:874px;top:164px;width:222px;height:48px;border:1px solid #555;background:#fff;font-size:13px;line-height:46px;padding-left:12px;color:#333}
.join{left:874px;top:227px;width:95px;height:47px;line-height:47px;background:var(--purple);color:#fff;text-align:center;font-family:"Poppins",sans-serif;font-weight:600;font-size:16px}
.country{left:891px;top:323px;width:222px;height:48px;border:1px solid #333;text-align:center;line-height:46px;font-size:15px;color:#222}
.copy{left:99px;top:415px;font-size:15px;color:#222}
.pay{left:829px;top:414px;display:flex;gap:8px}
.pay span{width:48px;height:24px;border-radius:3px;background:#fff;border:1px solid #ddd;display:block}
</style>
</head>
<body>
<div class="page">

  <header class="abs topbar">
    <div class="socials"><span></span><span></span><span></span><span></span></div>
    <div class="abs wholesale">
      <svg width="16" height="17" viewBox="0 0 16 17" fill="none" stroke="#fff" stroke-width="1.5"><circle cx="8" cy="5" r="3.5"/><path d="M1.5 16c0-3.6 2.9-6 6.5-6s6.5 2.4 6.5 6"/></svg>
      Register as a Wholesaler
      <svg width="20" height="20" viewBox="0 0 20 20" fill="none" stroke="#fff" stroke-width="1.5"><path d="M3 7h14l-1 12H4z"/><path d="M7 7V5a3 3 0 0 1 6 0v2"/></svg>
      <span class="cart-count">0</span>
    </div>
  </header>

  <nav class="abs nav">
    <div class="abs brand"><i></i>Kralto</div>
    <ul><li>Home</li><li>About Us</li><li>Pre-Workout</li><li>Creatine</li><li>Protein Shakes.</li></ul>
  </nav>

  <div class="abs promo">Annual SALE now on - Save up to 60%</div>

  <section class="abs hero">
    <div class="tub light" role="img" aria-label="White supplement tub"></div>
    <div class="tub dark" role="img" aria-label="Black supplement tub"></div>
    <h1>WELCOME TO KRALTO</h1>
    <p>FUELING HEALTH,NOT EXPENSES</p>
    <a class="btn">Apply Now Online</a>
  </section>

  <div class="abs cat" style="left:97px"><div class="bottle" role="img" aria-label="Supplement bottle"></div><h3>NEW ARRIVALS</h3><a class="btn">Shop Now</a></div>
  <div class="abs cat" style="left:444px"><div class="bottle" role="img" aria-label="Supplement bottle"></div><h3>NEW ARRIVALS</h3><a class="btn">Shop Now</a></div>
  <div class="abs cat" style="left:792px"><div class="bottle" role="img" aria-label="Supplement bottle"></div><h3>NEW ARRIVALS</h3><a class="btn">Shop Now</a></div>

  <h2 class="abs sec-title" style="top:1336px">OUR PRODUCTS</h2>
  <div class="abs rule" style="top:1390px"></div>
  <div class="abs viewall">View All</div>

  <div class="abs arrow" style="left:78px"><svg width="40" height="40"><path d="M22 14l-6 6 6 6" fill="none" stroke="#111" stroke-width="2"/></svg></div>
  <div class="abs prod" style="left:99px"><div class="ph"><b role="img" aria-label="Protein tub with shaker"></b></div><div class="name">Lorem ipsum dolor sit</div><div class="price">$135.00</div></div>
  <div class="abs prod" style="left:353px"><div class="ph"><b role="img" aria-label="Creatine tub"></b><span class="zoom"><svg width="40" height="40" fill="none" stroke="#111" stroke-width="1.5"><circle cx="19" cy="19" r="5"/><path d="M23 23l4 4"/></svg></span></div><div class="name">Lorem ipsum dolor sit</div><div class="price">$135.00</div></div>
  <div class="abs prod" style="left:606px"><div class="ph"><b role="img" aria-label="Whey protein tubs"></b></div><div class="name">Lorem ipsum dolor sit</div><div class="price">$135.00</div></div>
  <div class="abs prod" style="left:861px"><div class="ph"><b role="img" aria-label="Supplement bottles with capsules"></b></div><div class="name">Lorem ipsum dolor sit</div><div class="price">$135.00</div></div>
  <div class="abs arrow" style="left:1083px"><svg width="40" height="40"><path d="M18 14l6 6-6 6" fill="none" stroke="#111" stroke-width="2"/></svg></div>

  <section class="abs feature">
    <div class="abs photo1" role="img" aria-label="Woman holding a supplement bottle and phone"></div>
    <div class="abs photo2" role="img" aria-label="Smiling woman in sportswear pointing at a supplement"></div>
    <h2>FUELING HEALTH,<br>NOT EXPENSES</h2>
    <p>Lorem ipsum dolor sit amet, consectetur adipiscing elit, sed do eiusmod tempor incididunt ut labore et dolore magna aliqua. Ut enim ad minim veniam, quis nostrud exercitation ullamco laboris nisi ut aliquip ex ea commodo consequat.</p>
    <a class="btn btn-red">Shop Sale</a>
  </section>

  <h2 class="abs sec-title" style="top:2584px">RECENT POST</h2>
  <div class="abs rule" style="top:2632px"></div>

  <article class="abs post" style="left:99px"><div class="ph" role="img" aria-label="Woman in kitchen holding supplement" style="background:linear-gradient(135deg,#e6e4e0,#c9b98a 60%,#a8a39a)"></div><h4>Lorem ipsum dolor sit</h4><p>Lorem ipsum dolor sit amet, consectetur<br>incididunt ut labore et aliqua.</p></article>
  <article class="abs post" style="left:440px"><div class="ph" role="img" aria-label="Athlete resting beside protein powder" style="background:linear-gradient(135deg,#4a4440,#8a7a66 60%,#2e2a27)"></div><h4>Lorem ipsum dolor sit</h4><p>Lorem ipsum dolor sit amet, consectetur<br>incididunt ut labore et aliqua.</p></article>
  <article class="abs post" style="left:781px"><div class="ph" role="img" aria-label="Woman taking a supplement capsule" style="background:linear-gradient(135deg,#5e7a3a,#8c6a72 55%,#3c4a2a)"></div><h4>Lorem ipsum dolor sit</h4><p>Lorem ipsum dolor sit amet, consectetur<br>incididunt ut labore et aliqua.</p></article>

  <div class="abs thanks">THANKS FOR STOPPING BY - TAKE 20% OFF WITH CODE &nbsp;SAVE20</div>

  <footer class="abs footer">
    <div class="socials"><span></span><span></span><span></span><span></span></div>
    <div class="abs col" style="left:97px;width:320px"><h5>About</h5>Lorem ipsum dolor sit amet, consectetur adipiscing elit, sed do eiusmod tempor incididunt ut labore et dolore magna aliqua.</div>
    <div class="abs col" style="left:438px;width:110px"><h5>Info</h5>Login<br>Lost Password<br>Register as a<br>Wholesaler</div>
    <div class="abs col" style="left:577px"><h5>Explore</h5>Home<br>About Us<br>Pre-Workout<br>Creatine<br>Protein Shakes.</div>
    <div class="abs col" style="left:704px;width:120px"><h5>Quick links</h5>Contact Us<br>About Us<br>Terms of<br>Service<br>Privacy Policy</div>
    <div class="abs col" style="left:874px"><h5>Connect</h5>Join our mailing list for updates</div>
    <div class="abs email">Email Address</div>
    <div class="abs join">Join</div>
    <div class="abs country">United States (USD $) &nbsp;<svg width="10" height="12"><path d="M2 1l5 5-5 5" fill="none" stroke="#111" stroke-width="2"/></svg></div>
    <div class="abs copy">© 2023.Kralto .All Rights Reserved</div>
    <div class="abs pay"><span></span><span></span><span></span><span></span><span></span></div>
  </footer>

</div>
</body>
</html>
```